4 page brochure for Logistics Company

Need a 4 page brochure (ie folded A3) for a Logistics company.
Service is a virtual network of warehouse and logistics companies.
Style is professional but accessible.
We have logo and styles designed and will upload these.
We have identified example images that could be used in the brochure.
Content will be uploaded also.
Updates
Reason: A couple of designers requested more time
Am giving another 24 hours to finalise and will then select most suitable design
Target Market(s)
40 to 60 year old business owners (traditional) - Australian
Industry/Entity Type
It Company
Requirements
Must have
- Professional
Should not have
- Nothing tacky

```html
<!DOCTYPE html>
<html lang="en">
<head>
<meta charset="utf-8">
<title>Meridian Freight Network – Brochure Outer Spread</title>
<link rel="stylesheet" href="https://fonts.googleapis.com/css2?family=Open+Sans:ital,wght@0,400;0,700;1,400&family=Roboto:wght@500&display=swap">
<style>
  :root{
    --bg:#2a2a2a;
    --paper:#ffffff;
    --brand-blue:#1d4e94;
    --deep-blue:#1a4488;
    --bright-blue:#1e9ad6;
    --slate:#6a7f89;
    --ink:#111111;
    --white:#ffffff;
  }
  *{box-sizing:border-box;margin:0;padding:0}
  html,body{width:1200px;height:960px;overflow:hidden;background:var(--bg)}
  .spread{
    position:absolute;left:40px;top:84px;width:1120px;height:792px;
    background:var(--paper);overflow:hidden;
    font-family:"Open Sans",Arial,sans-serif;
  }
  .spread-art{position:absolute;inset:0;width:100%;height:100%}
  .brand{position:absolute;text-align:center}
  .brand-name{
    display:flex;align-items:center;gap:10px;
    font-family:"Open Sans",Arial,sans-serif;font-weight:700;
    color:var(--brand-blue);line-height:1.05;text-align:left;
  }
  .brand-mark{width:16px;height:16px;background:var(--brand-blue);flex:none}
  .tagline{
    font-family:"Roboto",Arial,sans-serif;font-weight:500;color:var(--ink);
    margin-top:10px;letter-spacing:.2px;white-space:nowrap;
  }
  .brand--back{left:36px;top:286px;width:300px}
  .brand--back .brand-name{font-size:27px;justify-content:center}
  .brand--back .tagline{font-size:18px}
  .brand--cover{left:850px;top:20px;width:260px}
  .brand--cover .brand-name{font-size:23px;justify-content:center}
  .brand--cover .tagline{font-size:16px;margin-top:8px}
  .headline{
    position:absolute;left:633px;top:540px;width:460px;
    font-weight:400;font-size:34px;line-height:41px;color:var(--white);
  }
  .intro{
    position:absolute;left:640px;top:645px;width:410px;
    font-style:italic;font-size:16.5px;line-height:21px;color:var(--white);text-align:center;
  }
  .web{
    position:absolute;left:740px;top:748px;width:220px;
    font-size:14px;color:var(--white);text-align:center;
  }
  .contacts{
    position:absolute;right:588px;top:674px;list-style:none;
    font-size:13px;color:var(--white);text-align:right;
  }
  .contacts li{display:flex;align-items:center;justify-content:flex-end;gap:8px;height:25px}
  .contacts svg{width:14px;height:14px;flex:none}
</style>
</head>
<body>
<main class="spread">
  <svg class="spread-art" viewBox="0 0 1251 882" preserveAspectRatio="none">
    <defs>
      <linearGradient id="photoTone" x1="0" y1="0" x2="1" y2="1">
        <stop offset="0" stop-color="#6b6f6a"/>
        <stop offset=".35" stop-color="#b9aa8e"/>
        <stop offset=".7" stop-color="#c9cfd4"/>
        <stop offset="1" stop-color="#aab4be"/>
      </linearGradient>
      <linearGradient id="photoFade" x1="0" y1="0" x2="1" y2="0">
        <stop offset="0" stop-color="#fff" stop-opacity="0"/>
        <stop offset="1" stop-color="#fff" stop-opacity=".75"/>
      </linearGradient>
      <linearGradient id="swoosh" x1="0" y1="0" x2="0" y2="1">
        <stop offset="0" stop-color="#1d4e94"/>
        <stop offset="1" stop-color="#1e9ad6"/>
      </linearGradient>
      <linearGradient id="blueWave" x1="0" y1="0" x2="1" y2="1">
        <stop offset="0" stop-color="#1e9ad6"/>
        <stop offset=".45" stop-color="#1a5fa8"/>
        <stop offset="1" stop-color="#1a4488"/>
      </linearGradient>
    </defs>
    <path role="img" aria-label="Photograph: warehouse interior with forklifts and tall pallet racking"
          d="M397,0 C470,180 560,380 627,520 L627,620 L1251,620 L1251,0 Z" fill="url(#photoTone)"/>
    <path d="M657,0 L1251,0 L1251,430 C1050,250 850,110 657,0 Z" fill="url(#photoFade)"/>
    <path class="swoosh" d="M307,0 L377,0 C430,150 500,300 567,412 C470,300 380,160 307,0 Z" fill="url(#swoosh)"/>
    <path class="wave-slate" d="M0,625 C200,540 450,495 650,500 C850,505 1050,450 1251,440 L1251,882 L0,882 Z" fill="var(--slate)"/>
    <path class="wave-blue" d="M60,882 C300,700 700,540 1251,487 L1251,882 Z" fill="url(#blueWave)"/>
    <path class="wave-edge" d="M60,882 C300,700 700,540 1251,487" fill="none" stroke="#fff" stroke-width="4"/>
  </svg>

  <section class="brand brand--back">
    <div class="brand-name"><span class="brand-mark"></span><span>Meridian Freight<br>Network</span></div>
    <p class="tagline">Reach : Savings : Growth</p>
  </section>

  <ul class="contacts">
    <li>07 3100 4820
      <svg viewBox="0 0 16 16"><path d="M2 6c0-3 12-3 12 0l-2 1-1-2H5L4 7 2 6zm2 2h8l1 5H3l1-5z" fill="#fff"/></svg></li>
    <li>0412 555 018
      <svg viewBox="0 0 16 16"><rect x="4" y="1" width="8" height="14" rx="1.5" fill="none" stroke="#fff" stroke-width="1.6"/><circle cx="8" cy="12.5" r=".9" fill="#fff"/></svg></li>
    <li>alex.hartley@meridianfreight.com.au
      <svg viewBox="0 0 16 16"><rect x="1" y="3" width="14" height="10" fill="#fff"/><path d="M1 3l7 6 7-6" fill="none" stroke="#1a5fa8" stroke-width="1.2"/></svg></li>
    <li>meridianfreight.com.au
      <svg viewBox="0 0 16 16"><circle cx="8" cy="8" r="6.5" fill="none" stroke="#fff" stroke-width="1.4"/><ellipse cx="8" cy="8" rx="2.8" ry="6.5" fill="none" stroke="#fff" stroke-width="1.2"/><path d="M1.5 8h13M3 4.5h10M3 11.5h10" stroke="#fff" stroke-width="1.1"/></svg></li>
  </ul>

  <section class="brand brand--cover">
    <div class="brand-name"><span class="brand-mark"></span><span>Meridian Freight<br>Network</span></div>
    <p class="tagline">Reach : Savings : Growth</p>
  </section>

  <h1 class="headline">A new solution for Australian warehouse business owners.</h1>
  <p class="intro">Offering national scale to increase revenues, achieving synergies to reduce costs, and enhancing the value in your business.</p>
  <p class="web">www.meridianfreight.com.au</p>
</main>
</body>
</html>
```